Business Card for KV

We need a double sided business card:

First Name Last Name
Cell 123-456-7890
firstname@emailaddress.com

License #1234-ABCD-4567
WFRSL # 12345
Alder Ridge County

```html
<!DOCTYPE html>
<html lang="en">
<head>
<meta charset="utf-8">
<title>Kindred Valley – Business Card</title>
<link rel="stylesheet" href="https://fonts.googleapis.com/css2?family=Bungee&display=swap">
<style>
  :root {
    --backdrop: #3a3a3a;
    --card-white: #ffffff;
    --navy: #2d4e69;
    --olive: #8f9440;
    --ink-light: #ffffff;
  }
  * { box-sizing: border-box; margin: 0; padding: 0; }
  html, body {
    width: 1189px;
    height: 1200px;
    overflow: hidden;
    background: var(--backdrop);
  }
  .stage {
    position: relative;
    width: 1189px;
    height: 1200px;
    display: flex;
    justify-content: center;
    align-items: center;
    gap: 70px;
  }
  .card {
    width: 430px;
    height: 640px;
    border-radius: 34px;
    position: relative;
    display: flex;
    flex-direction: column;
    align-items: center;
    justify-content: center;
    font-family: "Bungee", sans-serif;
    text-align: center;
  }
  .card--contact { background: var(--card-white); color: var(--navy); }
  .card--brand { background: var(--navy); }

  .person-name { font-size: 36px; letter-spacing: 1px; line-height: 1; white-space: nowrap; }
  .person-role { font-size: 17px; color: var(--olive); margin-top: 8px; }

  .detail-label {
    display: flex;
    align-items: center;
    gap: 12px;
    width: 290px;
    color: var(--olive);
    font-size: 15px;
    margin-top: 16px;
  }
  .detail-label::before,
  .detail-label::after {
    content: "";
    flex: 1;
    height: 1px;
    background: var(--olive);
  }
  .detail-value { font-size: 19px; margin-top: 4px; white-space: nowrap; }

  .credentials { margin-top: 22px; font-size: 17px; line-height: 1.3; white-space: nowrap; }

  .closing-rule {
    width: 290px;
    height: 2px;
    background: var(--olive);
    margin-top: 18px;
  }
  .leaf-ornament {
    width: 90px;
    height: 24px;
    background: var(--olive);
    border-radius: 0 0 45px 45px;
    margin-top: 2px;
  }

  .brand-mark {
    display: flex;
    align-items: center;
    gap: 14px;
    margin-top: -120px;
  }
  .brand-dot {
    width: 28px;
    height: 28px;
    border-radius: 50%;
    background: var(--olive);
  }
  .brand-name {
    font-size: 34px;
    line-height: 1.15;
    color: var(--ink-light);
    text-align: left;
  }
</style>
</head>
<body>
  <main class="stage">
    <section class="card card--contact" aria-label="Card back with contact details">
      <h1 class="person-name">Jordan Reyes</h1>
      <p class="person-role">Manager</p>

      <p class="detail-label">Cell</p>
      <p class="detail-value">123-456-7890</p>

      <p class="detail-label">Email</p>
      <p class="detail-value">firstname@email.com</p>

      <p class="credentials">
        License #1234-ABCD-4567<br>
        WFRSL # 12345<br>
        Alder Ridge County
      </p>

      <div class="closing-rule"></div>
      <div class="leaf-ornament" role="img" aria-label="Small olive leaf ornament"></div>
    </section>

    <section class="card card--brand" aria-label="Card front with company name">
      <div class="brand-mark">
        <span class="brand-dot"></span>
        <p class="brand-name">Kindred<br>Valley</p>
      </div>
    </section>
  </main>
</body>
</html>
```